Sleek modern site for stage hypnotist who does high school, college, university and corporate gigs.

Need a website design for stage hypnotist Mark Dolloway
I'm using a plinkio domain

Mark Dolloway is a stage hypnotist who does high school shows , colleges, corporate and fundraisers
Looking for something sleek and modern looking.
I need about 4 pages at least one main describing what i do
1st page Describes what events i do (high school, college, corporate, weddings, fundraisers, fairs)
2nd page would be an about/bio page
3rd FAQ page about hypnosis.

*what venues do you work with?
*how long is your show?
*How do we promote the show?
*is it safe
*are you insured?
*how much does it cost?
4th page will be a contact page and link to my social media like Snapvue, chirpnet, and possibly Friendlyn.

Included is a few pictures that I'll probably including on the site. I'm waiting on the rest for photoshoot at the this week. Some of these pictures probably will have different stock backgrounds other than grey (something like a las vegas strip or a stage.

Visually I'm looking for a cool color scheme.

Target Market(s)

High school for now but college and corporate down the road.

Industry/Entity Type

Entertainment Industry

Coding

Coded - Design and coding required

Number of Pages Required

4 page

Font styles to use
Serif
Sans Serif

Colors
3277b5
85acd3
9d9d9d
5c5c5c
cbcbcb
aaaaaa
1b1b1b
333333

Requirements
Must have
• MUST BE ABLE TO WORK WITH PLINKIO
• A sleek and professional look as if I've been doing this for years.
• The ability to edit the text of the site so i can improve upon the persuasive parts if need be.
• I also will be getting more promotional photos in the 5 or 6 days after the deadline days so if i pick your project i'd like to be able to integrate some of them into the design. The 3 photos i provided are somewhat place holders to give you an idea of the rest that are to come.
Nice to have
• drop down links
Should not have
• if you zoobit other stage hypnotists their sites are a bit stale and not that modern.

```html
<!DOCTYPE html>
<html lang="en">
<head>
<meta charset="utf-8">
<title>Mark Dolloway — Stage Hypnotist</title>
<link href="https://fonts.googleapis.com/css2?family=Yellowtail&family=Questrial&display=swap" rel="stylesheet">
<style>
  :root {
    --bg-top: #1c1c1c;
    --bg-mid: #141414;
    --bg-base: #030303;
    --text: #ffffff;
    --text-soft: #e6e6e6;
    --portrait-light: #4a4a52;
    --portrait-mid: #26262e;
    --portrait-dark: #0c0c10;
  }
  * { margin: 0; padding: 0; box-sizing: border-box; }
  html, body {
    width: 1200px;
    height: 1120px;
    overflow: hidden;
    background: var(--bg-base);
  }
  .page {
    position: relative;
    width: 1200px;
    height: 1120px;
    overflow: hidden;
    background: radial-gradient(ellipse at 70% 30%, #262626 0%, var(--bg-top) 35%, var(--bg-mid) 70%, #0a0a0a 100%);
    font-family: "Questrial", "Century Gothic", sans-serif;
    color: var(--text);
  }
  .base-band {
    position: absolute;
    left: 0; top: 808px;
    width: 1200px; height: 312px;
    background: var(--bg-base);
  }
  .portrait {
    position: absolute;
    left: 560px; top: 32px;
    width: 640px; height: 1024px;
    background:
      radial-gradient(ellipse 22% 14% at 62% 14%, #8a7468 0%, rgba(138,116,104,0) 100%),
      radial-gradient(ellipse 30% 18% at 38% 38%, #6e5a52 0%, rgba(110,90,82,0) 100%),
      radial-gradient(ellipse 55% 60% at 65% 65%, var(--portrait-light) 0%, var(--portrait-mid) 45%, var(--portrait-dark) 100%);
    -webkit-mask-image: radial-gradient(ellipse 65% 75% at 65% 55%, #000 55%, transparent 100%);
    mask-image: radial-gradient(ellipse 65% 75% at 65% 55%, #000 55%, transparent 100%);
  }
  .site-title {
    position: absolute;
    left: 115px; top: 105px;
    font-family: "Yellowtail", cursive;
    font-weight: 400;
    font-size: 68px;
    line-height: 1;
    letter-spacing: -1px;
  }
  .intro {
    position: absolute;
    left: 115px; top: 238px;
    width: 430px;
    font-size: 18px;
    line-height: 28.8px;
    color: var(--text);
  }
  .service {
    position: absolute;
    width: 225px;
  }
  .service h2 {
    font-family: "Yellowtail", cursive;
    font-weight: 400;
    font-size: 34px;
    line-height: 1;
    margin-bottom: 20px;
  }
  .service p {
    font-size: 13px;
    line-height: 24px;
    color: var(--text-soft);
  }
  .service--highschools { left: 110px; top: 528px; }
  .service--college { left: 371px; top: 528px; }
  .service--corporate { left: 642px; top: 516px; }
  .service--weddings { left: 904px; top: 512px; }
  .footer-nav {
    position: absolute;
    left: 123px; top: 948px;
    display: flex;
    align-items: center;
    gap: 18px;
    font-size: 17px;
    text-transform: uppercase;
  }
  .footer-nav a { color: var(--text); text-decoration: none; }
  .footer-nav .divider { font-size: 16px; }
</style>
</head>
<body>
<main class="page">
  <div class="base-band"></div>
  <div class="portrait" role="img" aria-label="Portrait photo of the hypnotist in glasses and a dark shirt, reaching one open hand toward the viewer"></div>

  <h1 class="site-title">Mark Dolloway</h1>
  <p class="intro">Mark Dolloway has over 12 years of entertaining from the streets to the stage for people of all walks of life in the Greater Toronto Area and Greater Hamilton! I have trained with some of the best in the industry and I not only use hypnosis to entertain but to help others as well!</p>

  <section class="service service--highschools">
    <h2>Highschools</h2>
    <p>Comedy hypnosis that will have your students laughing long after the show is finished Stage hypnosis is great for graduation, back to school, and even fundraising</p>
  </section>
  <section class="service service--college">
    <h2>College</h2>
    <p>Comedy hypnosis that will have your students laughing long after the show is finished Stage hypnosis is great for graduation, back to school, and even fundraising</p>
  </section>
  <section class="service service--corporate">
    <h2>Corporate</h2>
    <p>Comedy hypnosis that will have your students laughing long after the show is finished Stage hypnosis is great for graduation, back to school, and even fundraising</p>
  </section>
  <section class="service service--weddings">
    <h2>Weddings</h2>
    <p>Comedy hypnosis that will have your students laughing long after the show is finished Stage hypnosis is great for graduation, back to school, and even fundraising</p>
  </section>

  <nav class="footer-nav">
    <a href="#faq">FAQ</a>
    <span class="divider">|</span>
    <a href="#social">Social</a>
    <span class="divider">|</span>
    <a href="#contact">Contact</a>
  </nav>
</main>
</body>
</html>
```